Brolvane Co.,Ltd. need business card

Brolvane Company Limited is a facility management company. We provides a total solution services from administration, energy saving, security, safety, food catering to companies.

The logo should be in elegant style with innovative that suited to the upper market
Please see the logo image in the attached file. You can use this Red or Blue or Green checkerboard (color and font should be similar to logo) as the main part of business card (can be an entire of one side of business card) . In another side of card should contain contact details of personnel - here below demo information

Kanyarat Thoengsai
Chief Executive Officer

No.73, Soi 5, Ruam Wongsa Road
Nong Khaem, Bangkok,
10520, Thailand

Tel + 66841537296
Mobile + 66841537296
E-mail: Kanyarat.Thoengsai@brolvane-example.co.th

Target Market(s)

Factory, Hotel and Hospital

Industry/Entity Type

Business

Contact Information for Business Card

Kanyarat Thoengsai
Chief Executive Officer

Nong Khaem, Bangkok,
10520, Thailand

Tel + 66841537296
Mobile + 66841537296

We will change details with the winner designer

Font styles to use
Sans Serif

Requirements
Must have
• In style of red checkerboard and white color

```html
<!DOCTYPE html>
<html lang="en">
<head>
<meta charset="utf-8">
<title>Brolvane Co.,Ltd. business card</title>
<link rel="stylesheet" href="https://fonts.googleapis.com/css2?family=Ubuntu:wght@400;500;700&display=swap">
<style>
  :root {
    --backdrop: #e7e4df;
    --card-black: #1c1c1e;
    --card-black-soft: #2e2e31;
    --brand-red: #d8202c;
    --brand-red-deep: #a3121c;
    --brand-red-bright: #ee2f3a;
    --ink-white: #ffffff;
    --ink-soft: #f3d6d8;
  }
  * { margin: 0; padding: 0; box-sizing: border-box; }
  html, body {
    width: 1200px; height: 902px; overflow: hidden;
    background: var(--backdrop);
    font-family: "Ubuntu", Arial, sans-serif;
  }
  .canvas { position: relative; width: 1200px; height: 902px; }
  .card {
    position: absolute; top: 136px; width: 360px; height: 630px;
    background: var(--card-black); overflow: hidden;
    box-shadow: 0 10px 30px rgba(0,0,0,.25);
  }
  .card--front { left: 180px; }
  .card--back { left: 660px; }
  .card__shapes { position: absolute; inset: 0; }

  .brand-name {
    position: absolute; top: 70px; right: 36px;
    font-size: 44px; font-weight: 400; letter-spacing: 7px;
    color: var(--ink-white);
  }
  .email-band {
    position: absolute; left: 0; top: 432px; width: 360px; height: 34px;
    display: flex; align-items: center; gap: 10px; padding-left: 14px;
    color: var(--ink-white); font-size: 13px;
  }

  .name-band {
    position: absolute; top: 78px; right: 0; width: 220px; height: 66px;
    background: var(--brand-red); padding: 10px 16px 0 0; text-align: right;
    color: var(--ink-white);
  }
  .name-band__name { font-size: 19px; }
  .name-band__name strong { font-weight: 700; }
  .name-band__title { font-size: 14px; margin-top: 2px; }

  .contact-list { position: absolute; left: 44px; top: 250px; list-style: none; }
  .contact-item {
    display: flex; align-items: flex-start; gap: 12px;
    color: var(--ink-white); font-size: 15px; line-height: 1.3;
    margin-bottom: 18px;
  }
  .contact-item__icon {
    flex: none; width: 30px; height: 24px; background: var(--brand-red-bright);
    display: flex; align-items: center; justify-content: center;
  }
</style>
</head>
<body>
<main class="canvas">

  <section class="card card--front" aria-label="Card front">
    <svg class="card__shapes" viewBox="0 0 360 630" aria-hidden="true">
      <defs>
        <linearGradient id="redFrontFill" x1="0" y1="0" x2="1" y2="1">
          <stop offset="0" stop-color="#e3262f"/>
          <stop offset="1" stop-color="#a3121c"/>
        </linearGradient>
      </defs>
      <polygon points="0,0 360,0 360,630 258,630 0,150" fill="url(#redFrontFill)" role="img" aria-label="Red checkerboard area"/>
      <polygon points="0,150 258,630 0,630" fill="#1c1c1e"/>
      <polygon points="0,150 130,392 0,392" fill="#2e2e31"/>
    </svg>
    <div class="brand-name">BROLVANE</div>
    <div class="email-band" style="background:linear-gradient(90deg,var(--brand-red) 0%,var(--brand-red) 100%)">
      <svg width="18" height="13" viewBox="0 0 18 13" aria-hidden="true">
        <rect x="0.8" y="0.8" width="16.4" height="11.4" fill="none" stroke="#fff" stroke-width="1.5"/>
        <polyline points="1,1 9,7.5 17,1" fill="none" stroke="#fff" stroke-width="1.5"/>
      </svg>
      <span>Kanyarat.Thoengsai@brolvane-example.co.th</span>
    </div>
  </section>

  <section class="card card--back" aria-label="Card back">
    <svg class="card__shapes" viewBox="0 0 360 630" aria-hidden="true">
      <defs>
        <linearGradient id="redBackFill" x1="0" y1="0" x2="1" y2="1">
          <stop offset="0" stop-color="#e3262f"/>
          <stop offset="1" stop-color="#a3121c"/>
        </linearGradient>
      </defs>
      <polygon points="0,0 150,0 360,420 360,630 250,630 0,130" fill="url(#redBackFill)" role="img" aria-label="Red checkerboard stripe"/>
      <polygon points="0,130 250,630 0,630" fill="#2e2e31"/>
    </svg>
    <div class="name-band">
      <div class="name-band__name"><strong>Kanyarat</strong> Thoengsai</div>
      <div class="name-band__title">(C.E.O.)</div>
    </div>
    <ul class="contact-list">
      <li class="contact-item">
        <span class="contact-item__icon">
          <svg width="14" height="14" viewBox="0 0 24 24" aria-hidden="true"><path fill="#fff" d="M6.6 10.8a15 15 0 0 0 6.6 6.6l2.2-2.2c.3-.3.7-.4 1-.2 1.1.4 2.3.6 3.6.6.6 0 1 .4 1 1V20c0 .6-.4 1-1 1A17 17 0 0 1 3 4c0-.6.4-1 1-1h3.5c.6 0 1 .4 1 1 0 1.3.2 2.5.6 3.6.1.3 0 .7-.2 1z"/></svg>
        </span>
        <span>+ 66841537296</span>
      </li>
      <li class="contact-item">
        <span class="contact-item__icon">
          <svg width="10" height="15" viewBox="0 0 10 15" aria-hidden="true"><rect x="0.8" y="0.8" width="8.4" height="13.4" rx="1.5" fill="none" stroke="#fff" stroke-width="1.5"/><circle cx="5" cy="11.5" r="1" fill="#fff"/></svg>
        </span>
        <span>+ 66841537296</span>
      </li>
      <li class="contact-item">
        <span class="contact-item__icon">
          <svg width="12" height="16" viewBox="0 0 12 16" aria-hidden="true"><path fill="#fff" d="M6 0a6 6 0 0 0-6 6c0 4.5 6 10 6 10s6-5.5 6-10a6 6 0 0 0-6-6zm0 8.5A2.5 2.5 0 1 1 6 3.5a2.5 2.5 0 0 1 0 5z"/></svg>
        </span>
        <span>No.73, Soi 5, Ruam Wongsa Road<br>Nong Khaem, Bangkok,<br>10520, Thailand</span>
      </li>
    </ul>
  </section>

</main>
</body>
</html>
```